Startup Technology Consulting Firm in NYC Needs A Website

I need a website built for my startup technology consulting company Larkspur Systems Group. We offer a unique white glove service that provides end to end technology support. I want to stand out above the rest. We are small firm but are very dedicated which where we derive our name from LSG primarily offers
end to end technology advisory services to small businesses lacking their own IT staff. We offer top notch white glove and our customer service and satisfaction is exceed by no one.

Below are some of what we provide our clients

Strategic IT Planning
Business Continuity Planning/Disaster Recovery
Cloud Computing\DataCenter Solutions
Server Infrastructure/Networking
Virtualization Technologies
Project Management

Our Technology Advisors hold many certifications from Quorvane & Zelpix. We are also Quorvane Partners

I have attached my logo (preview design) As soon as I ge the final images I will upload.

Industry/Entity Type

Information Technology

Coding

Coded - Design and coding required

Number of Pages Required

1 page

Font styles to use
Sans Serif

Requirements
Must have
• Attract Target Market. The site should bleed the company vision
• DEDICATION everything about the site should show this
• Layout the Benefits of our offerings
• Links to my social media
• Links to dircct my client's for remote support

```html
<!DOCTYPE html>
<html lang="en">
<head>
<meta charset="utf-8">
<title>Larkspur Systems Group — Services</title>
<link rel="stylesheet" href="https://fonts.googleapis.com/css2?family=Open+Sans:wght@300;400;600&display=swap">
<style>
  :root {
    --ink: #1a1a1a;
    --blue: #1166b0;
    --blue-dark: #0b5aa2;
    --green: #7ab83a;
    --green-edge: #5e9a26;
    --ice-1: #dfeef1;
    --ice-2: #f3fbfc;
    --ice-3: #cfe3e8;
    --sky-1: #bcdcec;
    --sky-2: #f6f9fb;
    --white: #ffffff;
  }
  * { box-sizing: border-box; margin: 0; padding: 0; }
  html, body { width: 1200px; height: 1200px; overflow: hidden; background: var(--white); }
  body { position: relative; font-family: "Open Sans", Arial, sans-serif; color: var(--ink); }

  .section-title {
    position: absolute; left: 0; width: 1200px; text-align: center;
    font-weight: 300; font-size: 35px; letter-spacing: -0.3px; line-height: 1;
  }
  .section-title .accent { color: var(--blue); }

  .services {
    position: absolute; left: 78px; top: 0; width: 1024px; height: 519px;
    background:
      radial-gradient(ellipse 420px 300px at 55% 45%, var(--ice-2), transparent 70%),
      linear-gradient(135deg, var(--ice-1) 0%, var(--ice-2) 45%, var(--ice-3) 100%);
    overflow: hidden;
  }
  .services .deco { position: absolute; inset: 0; }
  .services .section-title { left: -78px; top: 64px; }

  .service { position: absolute; width: 260px; text-align: center; }
  .service-icon {
    width: 93px; height: 93px; margin: 0 auto; border: 1.5px solid var(--blue);
    border-radius: 50%; display: flex; align-items: center; justify-content: center;
    background: rgba(255,255,255,0.15);
  }
  .service-icon svg { width: 50px; height: 50px; }
  .service-icon .figure-fill {
    width: 50px; height: 44px; border-radius: 50%;
    background: radial-gradient(circle, var(--blue) 0%, var(--blue-dark) 60%, rgba(17,102,176,0.2) 100%);
  }
  .service-label { margin-top: 14px; font-size: 14.5px; line-height: 22px; color: var(--ink); }

  .benefits .section-title { top: 577px; }
  .benefits-intro {
    position: absolute; left: 0; width: 1200px; top: 622px; text-align: center;
    font-size: 12.6px; line-height: 21.5px;
  }
  .benefit-list { position: absolute; left: 122px; top: 690px; width: 920px; list-style: none; }
  .benefit-list li {
    position: relative; padding-left: 32px; font-size: 12.6px; line-height: 21.5px;
  }
  .benefit-list li svg { position: absolute; left: 0; top: 5px; width: 27px; height: 12px; }

  .remote-btn {
    position: absolute; left: 393px; top: 956px; width: 396px; height: 51px;
    background: var(--green); border-bottom: 2px solid var(--green-edge);
    color: var(--white); font-weight: 600; font-size: 19px; text-decoration: none;
    display: flex; align-items: center; justify-content: center; gap: 10px; letter-spacing: 0.2px;
  }

  .certifications {
    position: absolute; left: 78px; top: 1051px; width: 1024px; height: 149px;
    background:
      radial-gradient(ellipse 500px 260px at 50% 70%, var(--sky-2) 55%, transparent 80%),
      linear-gradient(90deg, var(--sky-1) 0%, var(--sky-2) 30%, var(--sky-2) 70%, var(--sky-1) 100%);
    overflow: hidden;
  }
  .certifications .section-title { left: -78px; top: 63px; }
  .cert-divider { position: absolute; top: 131px; width: 0; height: 20px; border-left: 1px dashed #555; }
</style>
</head>
<body>

<section class="services">
  <svg class="deco" viewBox="0 0 1024 519" fill="none" stroke="#ffffff" stroke-width="2" opacity="0.7">
    <path d="M395 38 V12 H620 V38"/>
    <path d="M560 30 H700 V80 H700"/>
    <path d="M975 140 H1020"/>
    <path d="M1000 200 H1024"/>
    <path d="M80 420 V440 H250"/>
    <path d="M610 470 H780 V519"/>
    <path d="M780 483 H820 V519"/>
    <path d="M960 505 H1024"/>
    <path d="M0 310 H60"/>
  </svg>
  <h2 class="section-title">OUR <span class="accent">SERVICES</span></h2>

  <div class="service" style="left:62px;top:143px">
    <div class="service-icon">
      <svg viewBox="0 0 50 50" fill="none" stroke="#1166b0" stroke-width="2.4">
        <rect x="10" y="4" width="26" height="40" rx="3"/>
        <rect x="14" y="9" width="18" height="28" stroke-width="1.5"/>
        <path d="M19 14 h6 v5 h-6z M22 19 v5 M18 27 a2 2 0 1 0 0.1 0 M22 24 l-3 3" stroke-width="1.4"/>
        <path d="M28 30 l6 -4 l8 8 l-6 6 h-8z" fill="#1166b0" stroke="none"/>
      </svg>
    </div>
    <div class="service-label">Strategic IT Planning</div>
  </div>

  <div class="service" style="left:382px;top:143px">
    <div class="service-icon"><div class="figure-fill" role="img" aria-label="Team of people exchanging work in a cycle"></div></div>
    <div class="service-label">Business Continuity<br>Planning/Disaster Recovery</div>
  </div>

  <div class="service" style="left:702px;top:143px">
    <div class="service-icon">
      <svg viewBox="0 0 50 50" fill="none" stroke="#1166b0" stroke-width="2.2">
        <path d="M12 22 a8 8 0 0 1 8 -10 a10 10 0 0 1 18 4 a6 6 0 0 1 2 8"/>
        <rect x="9" y="20" width="9" height="18" fill="#1166b0"/>
        <rect x="20.5" y="23" width="9" height="18" fill="#1166b0"/>
        <rect x="32" y="20" width="9" height="18" fill="#1166b0"/>
        <path d="M11 25 h5 M11 29 h5 M22.5 28 h5 M22.5 32 h5 M34 25 h5 M34 29 h5" stroke="#ffffff" stroke-width="1.4"/>
      </svg>
    </div>
    <div class="service-label">Cloud Computing\DataCenter<br>Solutions</div>
  </div>

  <div class="service" style="left:62px;top:319px">
    <div class="service-icon">
      <svg viewBox="0 0 50 50" fill="none" stroke="#1166b0" stroke-width="2.2">
        <rect x="18" y="5" width="14" height="10"/><path d="M22 18 h6"/>
        <path d="M25 18 v26 M10 30 v-4 h30 v4"/>
        <rect x="5" y="30" width="13" height="10"/><rect x="32" y="30" width="13" height="10"/>
        <path d="M3 44 h17 M30 44 h17"/>
      </svg>
    </div>
    <div class="service-label">Server Infrastructure/Networking</div>
  </div>

  <div class="service" style="left:382px;top:319px">
    <div class="service-icon">
      <svg viewBox="0 0 50 50" fill="none" stroke="#1166b0" stroke-width="2.2">
        <circle cx="12" cy="8" r="3" fill="#1166b0" stroke="none"/>
        <path d="M7 18 h10 M12 12 v14"/>
        <path d="M28 16 a5 5 0 0 1 5 -6 a6 6 0 0 1 11 3 a4 4 0 0 1 -1 7 h-14 a4 4 0 0 1 -1 -4z" fill="#1166b0"/>
        <path d="M20 16 h6" stroke-dasharray="2 2"/>
        <rect x="6" y="28" width="16" height="11"/><path d="M11 43 h6"/>
        <rect x="34" y="26" width="10" height="20"/><path d="M36 31 h6 M36 35 h6"/>
        <path d="M23 34 h10" stroke-dasharray="2 2"/>
      </svg>
    </div>
    <div class="service-label">Virtualization Technologies</div>
  </div>

  <div class="service" style="left:702px;top:319px">
    <div class="service-icon"><div class="figure-fill" role="img" aria-label="Group of business people"></div></div>
    <div class="service-label">Project Management</div>
  </div>
</section>

<section class="benefits">
  <h2 class="section-title">BENEFITS OF <span class="accent">OUR OFFERINGS</span></h2>
  <p class="benefits-intro">Lorem ipsum dolor sit amet, consectetur adipiscing elit. Donec venenatis vehicula rhoncus. Sspendisse ultricies posuere euismod.<br>Quisque rutrum sollicitudin faucibus.</p>
  <ul class="benefit-list">
    <li style="margin-bottom:6px"><svg viewBox="0 0 27 12" fill="#1166b0"><rect x="0" y="3" width="2" height="6"/><rect x="4" y="3" width="2" height="6"/><rect x="8" y="3" width="2" height="6"/><rect x="12" y="3" width="5" height="6"/><path d="M17 0 L26 6 L17 12z"/></svg>Lorem ipsum dolor sit amet, consectetur adipiscing elit. Donec venenatis vehicula rhoncus. Sspendisse ultricies posuere euismod. Quisque rutrum sollicitudin faucibus.</li>
    <li style="margin-bottom:7px"><svg viewBox="0 0 27 12" fill="#1166b0"><rect x="0" y="3" width="2" height="6"/><rect x="4" y="3" width="2" height="6"/><rect x="8" y="3" width="2" height="6"/><rect x="12" y="3" width="5" height="6"/><path d="M17 0 L26 6 L17 12z"/></svg>Lorem ipsum dolor sit amet, consectetur adipiscing elit. Donec venenatis vehicula rhoncus. Sspendisse ultricies posuere euismod. Quisque rutrum sollicitudin faucibus.</li>
    <li style="margin-bottom:11px"><svg viewBox="0 0 27 12" fill="#1166b0"><rect x="0" y="3" width="2" height="6"/><rect x="4" y="3" width="2" height="6"/><rect x="8" y="3" width="2" height="6"/><rect x="12" y="3" width="5" height="6"/><path d="M17 0 L26 6 L17 12z"/></svg>Lorem ipsum dolor sit amet, consectetur adipiscing elit. Donec venenatis vehicula rhoncus. Sspendisse ultricies posuere euismod. Quisque rutrum sollicitudin faucibus.</li>
    <li style="margin-bottom:6px"><svg viewBox="0 0 27 12" fill="#1166b0"><rect x="0" y="3" width="2" height="6"/><rect x="4" y="3" width="2" height="6"/><rect x="8" y="3" width="2" height="6"/><rect x="12" y="3" width="5" height="6"/><path d="M17 0 L26 6 L17 12z"/></svg>Lorem ipsum dolor sit amet, consectetur adipiscing elit. Donec venenatis vehicula rhoncus. Sspendisse ultricies posuere euismod. Quisque rutrum sollicitudin faucibus.</li>
    <li><svg viewBox="0 0 27 12" fill="#1166b0"><rect x="0" y="3" width="2" height="6"/><rect x="4" y="3" width="2" height="6"/><rect x="8" y="3" width="2" height="6"/><rect x="12" y="3" width="5" height="6"/><path d="M17 0 L26 6 L17 12z"/></svg>Lorem ipsum dolor sit amet, consectetur adipiscing elit. Donec venenatis vehicula rhoncus. Sspendisse ultricies posuere euismod. Quisque rutrum sollicitudin faucibus.</li>
  </ul>
  <a class="remote-btn" href="#remote-support">CLICK HERE FOR REMOTE SUPPORT
    <svg width="17" height="14" viewBox="0 0 17 14" fill="none" stroke="#ffffff" stroke-width="2.6"><path d="M2 1 l6 6 l-6 6 M9 1 l6 6 l-6 6"/></svg>
  </a>
</section>

<section class="certifications">
  <svg class="deco" viewBox="0 0 1024 149" fill="none" stroke="#ffffff" stroke-width="14" opacity="0.55" style="position:absolute;inset:0">
    <path d="M470 0 Q380 120 360 149"/>
    <path d="M820 0 Q880 90 900 149"/>
  </svg>
  <h2 class="section-title">OUR CERTIFICATIONS <span class="accent">AND AFFILIATIONS</span></h2>
  <span class="cert-divider" style="left:352px"></span>
  <span class="cert-divider" style="left:672px"></span>
</section>

</body>
</html>
```